Digital Marketing Website Redesign, modern, fresh, dynamic

Hi there, we would like to freshen up our website and create a new dynamic look. We are a digital marketing agency who specialise in digital transformation in the form of creating websites for appointment bookings. Our clients are service businesses such as hairdressers, dentists and doctors who's patients need to book appointments with them.

Our company name is Plombek with the point being we can help increase your revenue curve by increasing your appointment bookings.

Our services include building the website, creating campaigns to drive traffic, increasing conversions and monitoring and reporting.

We are playing with a tagline of 'Step into your Digital Transformation' as we have a 5 step journey that customers can take with us getting them from zero to full appointment bookings.

Our current website is www.plomnbek-site.example

You can see a draft design that I mocked up on Canva here https://www.drawpadhub.example/design/QXT82LmnB7K/PoWz41kdRtGyvb_sxE_JNq/edit?utm_content=QXT82LmnB7K&utm_campaign=designshare&utm_medium=link2&utm_source=sharebutton

Also attached some other homepage ideas. In regard to photos we are open to ideas.

Please let if you need any more information to provide us with an initial design. Thanks million and I look forward to receiving fantastic designs :)

Marissa Tobler
Plombek

Target Market(s)

Appointment based businesses such as hairdressers, dentists, doctors

Industry/Entity Type

Marketing and Digital

Coding

Coded - Design and coding required

Number of Pages Required

1 page

Colors
0094D4
00A9DD
6FCCEA
C7EBF8
E9F6FB

Requirements
Must have
• Appointment booking CTA
Nice to have
• A website we like https://www.morwenhalbrook.example

```html
<!DOCTYPE html>
<html lang="en">
<head>
<meta charset="utf-8">
<title>Plombek – Digital Marketing</title>
<link href="https://fonts.googleapis.com/css2?family=DM+Serif+Display&family=Poppins:wght@300;400;500;600;700&display=swap" rel="stylesheet">
<style>
:root{
  --blue:#0094d4;
  --blue-bright:#00a9dd;
  --sky:#6fccea;
  --pale:#c7ebf8;
  --mist:#e9f6fb;
  --deep:#0a5b8c;
  --ink:#1f3a52;
  --muted:#6f8393;
  --white:#ffffff;
  --line:#d5e9f2;
  --star:#f2a01b;
}
*{box-sizing:border-box;margin:0;padding:0}
html,body{width:1200px;height:4841px;overflow:hidden}
body{position:relative;background:var(--mist);font-family:"Poppins",sans-serif;color:var(--ink)}
.abs{position:absolute}
.serif{font-family:"DM Serif Display",serif;color:var(--deep);font-weight:400}
.eyebrow{font-size:11px;font-weight:500;color:var(--blue-bright);letter-spacing:.3px;display:flex;align-items:center;gap:14px;text-transform:uppercase}
.eyebrow::after{content:"";width:50px;height:2px;background:var(--blue-bright)}
.body-copy{font-size:12.5px;line-height:24px;color:var(--muted);font-weight:300}
.btn-primary{background:var(--blue);color:#fff;font-size:12px;font-weight:600;border-radius:4px;display:flex;align-items:center;justify-content:center}

/* header */
.topbar{left:0;top:0;width:1200px;height:34px;background:var(--mist)}
.header{left:0;top:34px;width:1200px;height:54px;background:#fff}
.welcome{left:394px;top:11px;font-size:12px;color:var(--ink)}
.top-mail{left:628px;top:6px;display:flex;align-items:center;gap:8px;font-size:12px;color:var(--ink)}
.logo-bubble{left:138px;top:2px;width:172px;height:80px;border-radius:50%;background:#fff;box-shadow:0 4px 12px rgba(0,80,120,.1);display:flex;align-items:center;justify-content:center}
.logo-text{font-weight:700;font-size:26px;color:var(--blue)}
.nav{left:337px;top:53px;display:flex;gap:38px;font-size:12px;color:var(--ink)}
.nav .active{color:var(--blue);font-weight:600}
.call{left:857px;top:0;width:202px;height:88px;background:var(--blue);color:#fff;padding:18px 0 0 44px}
.call small{display:block;font-size:12px}
.call b{font-size:19px;font-weight:600}
.call-icon{top:28px;width:34px;height:34px;border-radius:50%;background:#fff;border:2px solid var(--sky);display:flex;align-items:center;justify-content:center}

/* hero */
.hero{left:0;top:88px;width:1200px;height:776px;background:radial-gradient(circle at 72% 40%,#e9f6fb 0%,#6fccea 14%,#00a9dd 30%,#0a5b8c 62%,#06314f 95%)}
.hero-card{left:77px;top:272px;width:601px;height:361px;background:#fff;padding:48px 0 0 45px}
.hero-card::before{content:"";position:absolute;left:0;top:60px;width:6px;height:98px;background:var(--blue-bright)}
.hero-card h1{font-size:58px;line-height:66px}
.hero-card p{margin-top:22px;width:420px;font-size:11px;line-height:22px;color:var(--muted)}
.hero-card .btn-primary{margin-top:26px;width:190px;height:46px}

/* about */
.about-text{left:623px;top:990px;width:450px}
.about-text h2{font-size:36px;line-height:56px;margin-top:22px}
.about-text .body-copy{margin-top:18px;font-size:12px}
.about-text .btn-primary{margin-top:22px;width:168px;height:46px}

.features{left:90px;top:1531px;width:1014px;height:215px;background:#fff;border-radius:0 0 80px 80px;box-shadow:0 6px 20px rgba(0,80,120,.06);display:flex;padding:36px 0 0 56px;gap:42px}
.feature{display:flex;gap:14px;width:270px}
.f-icon{width:62px;height:62px;border-radius:50%;border:2px solid var(--blue);flex:none;display:flex;align-items:center;justify-content:center}
.feature h3{font-size:21px}
.feature .sub{color:var(--blue-bright);font-size:14px}
.feature p{font-size:11.5px;line-height:22px;color:#4f6272;margin-top:8px;font-weight:300}

/* services */
.svc-head{left:95px;top:1853px}
.svc-title{left:95px;top:1885px;font-size:40px}
.arrow-btn{top:1870px;width:44px;height:62px;background:#fff;box-shadow:0 2px 8px rgba(0,80,120,.12);display:flex;align-items:center;justify-content:center}
.svc-card{top:1974px;width:323px;height:375px}
.svc-photo{position:absolute;left:0;top:0;width:323px;height:234px;border-radius:22px 22px 0 0}
.svc-box{position:absolute;left:20px;top:176px;width:283px;height:199px;background:#fff;padding:26px 0 0 39px;box-shadow:0 4px 14px rgba(0,80,120,.1)}
.svc-box h3{font-size:20px}
.svc-box p{font-size:11.5px;line-height:24px;color:#4f6272;margin-top:12px;width:220px;font-weight:300}
.svc-box a{display:block;margin-top:14px;font-size:14px;font-weight:600;color:var(--blue);text-decoration:none}
.svc-box.feature-box{background:var(--blue)}
.svc-box.feature-box h3,.svc-box.feature-box p,.svc-box.feature-box a{color:#fff}
.outline-btn{left:513px;top:2392px;width:168px;height:46px;border:2px solid var(--blue);border-radius:4px;font-size:13px;font-weight:600;color:var(--blue);display:flex;align-items:center;justify-content:center}

/* why */
.why{left:0;top:2524px;width:1200px;height:637px;background:#fff}
.why-head{left:93px;top:2610px}
.why-title{left:92px;top:2640px;font-size:42px;line-height:62px;width:480px}
.why-copy{left:93px;top:2775px;width:450px;font-size:11.5px;line-height:24px}
.why-item{width:250px;display:flex;gap:22px}
.why-item h4{font-size:14px;font-weight:600;color:var(--deep)}
.why-item p{font-size:11.5px;line-height:24px;color:var(--muted);margin-top:6px;font-weight:300}

/* reviews */
.rev-head{left:0;top:3220px;width:1200px;display:flex;justify-content:center}
.rev-head .eyebrow::before{content:"";width:50px;height:2px;background:var(--blue-bright)}
.rev-title{left:0;top:3250px;width:1200px;text-align:center;font-size:42px}
.review{top:3390px;width:322px;height:263px;background:#fff;box-shadow:0 2px 10px rgba(0,80,120,.06);text-align:center}
.avatar{position:absolute;left:131px;top:-22px;width:60px;height:60px;border-radius:50%;background:linear-gradient(var(--pale),var(--blue))}
.stars{margin-top:78px;color:var(--star);font-size:16px;letter-spacing:9px}
.review p{font-size:12px;line-height:24px;color:#4f6272;margin:14px auto 0;width:220px;font-weight:300}
.quote{position:absolute;left:128px;top:233px;width:66px;height:66px;border-radius:50%;background:var(--blue);border:6px solid var(--mist);color:#fff;font-family:"DM Serif Display",serif;font-size:34px;line-height:58px}
.rev-name{top:3688px;width:322px;text-align:center;font-size:16px;font-weight:600;color:var(--ink)}
.rev-name small{display:block;font-size:12px;font-weight:300;color:var(--muted);margin-top:4px}

/* contact */
.contact-band{left:0;top:3897px;width:1200px;height:501px;background:linear-gradient(90deg,#3f6f8c,#8fb7c9 35%,#dceef5 70%,#c7ebf8)}
.contact-person{left:170px;top:3756px;width:440px;height:642px;border-radius:200px 200px 0 0;background:linear-gradient(#6b4a35,#eef2f4 40%,#b89468 85%)}
.form-card{left:648px;top:3977px;width:466px;height:478px;border-radius:28px;background:#fff;padding:6px}
.form-inner{width:100%;height:100%;border-radius:24px;background:var(--blue);padding:34px 34px 0;text-align:center;color:#fff}
.form-inner h2{font-size:27px;font-weight:600}
.form-inner p{font-size:11.5px;line-height:17px;margin-top:12px}
.field{margin-top:24px;height:44px;border-radius:4px;background:rgba(255,255,255,.2);text-align:left;font-size:9px;padding:15px 0 0 28px;letter-spacing:.3px}
.field:first-of-type{margin-top:28px}
.submit{margin-top:32px;height:46px;border-radius:4px;background:#fff;color:var(--blue);font-size:15px;font-weight:600;display:flex;align-items:center;justify-content:center}

/* footer */
.foot-logo{left:112px;top:4567px;font-size:44px;font-weight:700;color:var(--blue)}
.follow{left:112px;top:4680px;display:flex;align-items:center;gap:10px;font-size:14px;color:var(--deep);font-weight:500}
.soc{width:26px;height:26px;border-radius:50%;background:var(--pale)}
.fcol h5{font-size:14px;font-weight:500;color:var(--deep);padding-bottom:10px;border-bottom:1px solid var(--line);width:120px}
.fcol ul{list-style:none;font-size:13px;color:var(--muted);line-height:32px;margin-top:10px}
.fcol .row{display:flex;gap:16px;align-items:flex-start;font-size:13px;color:var(--muted);line-height:22px;margin-top:14px}
.news-in{margin-top:14px;display:flex;width:248px;height:34px;border:1px solid var(--line)}
.news-in span{flex:1;font-size:10px;color:#999;padding:10px 14px;background:#fff}
.news-in b{width:100px;background:var(--blue);color:#fff;font-size:12px;font-weight:600;display:flex;align-items:center;justify-content:center}
.foot-line{left:112px;top:4787px;width:986px;height:1px;background:var(--line)}
.copy{left:0;top:4808px;width:1200px;text-align:center;font-size:12px;color:var(--deep)}
</style>
</head>
<body>

<!-- header -->
<div class="abs topbar"></div>
<div class="abs header"></div>
<div class="abs welcome">WELCOME</div>
<div class="abs top-mail">
  <svg width="24" height="24" viewBox="0 0 24 24"><circle cx="12" cy="12" r="11" fill="none" stroke="#0094d4" stroke-width="2"/><rect x="6.5" y="8" width="11" height="8" fill="#0094d4"/><path d="M6.5 8l5.5 4.5L17.5 8" stroke="#fff" fill="none" stroke-width="1.2"/></svg>
  hello@plombek-mail.example
</div>
<div class="abs logo-bubble"><span class="logo-text">Plombek</span></div>
<nav class="abs nav"><span class="active">HOME</span><span>About Us</span><span>Services</span><span>Our team</span><span>Gallery</span><span>Contact Us</span></nav>
<div class="abs call"><small>Book today at</small><b>(555) 014-2287</b></div>
<div class="abs call-icon" style="left:840px">
  <svg width="16" height="16" viewBox="0 0 24 24"><path d="M6 2l4 4-2 3a12 12 0 0 0 7 7l3-2 4 4-3 4C10 22 2 14 2 5z" fill="#00a9dd"/></svg>
</div>

<!-- hero -->
<div class="abs hero" role="img" aria-label="Person walking through a glowing blue digital tunnel"></div>
<svg class="abs" style="left:0;top:740px" width="1200" height="130" viewBox="0 0 1200 130">
  <path d="M0 40 C220 120 420 110 640 60 C860 10 1060 0 1200 70 L1200 130 L0 130Z" fill="#e9f6fb"/>
  <path d="M0 52 C230 130 430 110 650 56 C850 8 1050 -4 1200 60 L1200 72 C1050 14 860 24 660 74 C440 128 220 136 0 70Z" fill="#6fccea"/>
  <path d="M700 46 C880 0 1060 -4 1200 58 L1200 66 C1060 10 890 14 720 50Z" fill="#0094d4"/>
</svg>
<div class="abs hero-card">
  <h1 class="serif">Elevate Your<br>Brand</h1>
  <p>Lorem ipsum dolor sit amet, consectetur adipiscing elit, sed do eiusmod tempor incididunt ut labore et dolore magna aliqua. Ut enim</p>
  <div class="btn-primary">Book Appointment</div>
</div>

<!-- about -->
<div class="abs" style="left:105px;top:972px;width:303px;height:315px;border-radius:70px 0 0 0;background:linear-gradient(135deg,#2e4656,#a7bcc8 60%,#e9f6fb)" role="img" aria-label="Team of colleagues working together in an office"></div>
<div class="abs" style="left:430px;top:992px;width:120px;height:120px;border-radius:40px 0 40px 0;background:linear-gradient(135deg,#4d6a7e,#c7ebf8)" role="img" aria-label="Small team meeting around a table"></div>
<div class="abs" style="left:268px;top:1132px;width:304px;height:316px;border-radius:0 0 90px 0;background:linear-gradient(135deg,#c7ebf8,#0094d4 55%,#0a3c5c)" role="img" aria-label="Hands on a laptop with digital marketing icons"></div>
<div class="abs" style="left:252px;top:1170px;width:86px;height:86px;border-radius:50%;background:var(--blue);border:4px solid #fff;display:flex;align-items:center;justify-content:center;color:#fff;font-size:13px;font-weight:600">Plombek</div>
<div class="abs about-text">
  <div class="eyebrow">About us</div>
  <h2 class="serif">Digital Excellence,<br>Marketing Brilliance</h2>
  <p class="body-copy">Lorem ipsum dolor sit amet, consectetur adipiscing elit, sed do eiusmod tempor incididunt ut labore et dolore magna aliqua. Ut enim ad min im veniam, quis nostrud exercitation ullamco laboris nisi ut aliquip ex ea commodo consequat. Duis aute irure dolor in reprehenderit in voluptate velit esse cillum dolore eu fugiat nulla pariatur. Excepteur sint occaecat cupidatat non proident, sunt in culpa qui officia deserunt mollit anim id est laborum.</p>
  <div class="btn-primary">Learn More</div>
</div>

<div class="abs features">
  <div class="feature">
    <div class="f-icon"><svg width="30" height="30" viewBox="0 0 30 30"><circle cx="15" cy="15" r="10" fill="none" stroke="#0094d4" stroke-width="2" stroke-dasharray="3 3"/><circle cx="15" cy="15" r="3" fill="#00a9dd"/></svg></div>
    <div><h3 class="serif">Expertise</h3><div class="sub">Learn More</div><p>Lorem ipsum dolor sit amet, consectetur adipiscing elit, se do eiusmod tempor e</p></div>
  </div>
  <div class="feature">
    <div class="f-icon"><svg width="30" height="30" viewBox="0 0 30 30"><path d="M15 5v20M5 15h20" stroke="#0094d4" stroke-width="2" stroke-dasharray="4 3"/><circle cx="15" cy="15" r="3" fill="#00a9dd"/></svg></div>
    <div><h3 class="serif">Experience</h3><div class="sub">Learn More</div><p>Lorem ipsum dolor sit amet, consectetur adipiscing elit, se do eiusmod tempor e</p></div>
  </div>
  <div class="feature">
    <div class="f-icon"><svg width="30" height="30" viewBox="0 0 30 30"><path d="M7 17a8 8 0 0 1 16 0" fill="none" stroke="#0094d4" stroke-width="2"/><rect x="6" y="16" width="5" height="7" rx="2" fill="#0094d4"/><rect x="19" y="16" width="5" height="7" rx="2" fill="#0094d4"/></svg></div>
    <div><h3 class="serif">Professionalism</h3><div class="sub">Learn More</div><p>Lorem ipsum dolor sit amet, consectetur adipiscing elit, se do eiusmod tempor e</p></div>
  </div>
</div>

<!-- services -->
<div class="abs eyebrow svc-head">Services</div>
<h2 class="abs serif svc-title">Our Services</h2>
<div class="abs arrow-btn" style="left:1007px"><svg width="12" height="12" viewBox="0 0 12 12"><path d="M8 1L3 6l5 5" stroke="#1f3a52" stroke-width="2" fill="none"/></svg></div>
<div class="abs arrow-btn" style="left:1058px"><svg width="12" height="12" viewBox="0 0 12 12"><path d="M4 1l5 5-5 5" stroke="#1f3a52" stroke-width="2" fill="none"/></svg></div>

<div class="abs svc-card" style="left:90px">
  <div class="svc-photo" style="background:linear-gradient(135deg,#0a3c5c,#6fccea 50%,#0a5b8c)" role="img" aria-label="Hand touching a digital marketing interface"></div>
  <div class="svc-box"><h3 class="serif">Marketing Services</h3><p>Lorem ipsum dolor sit amet, consectetur adipiscing elit, sed do eiusmod tempor incididunt ut nn</p><a>Read More</a></div>
</div>
<div class="abs svc-card" style="left:436px">
  <div class="svc-photo" style="background:linear-gradient(135deg,#0a5b8c,#00a9dd 50%,#0a3c5c)" role="img" aria-label="Person booking an appointment on a laptop"></div>
  <div class="svc-box feature-box"><h3 class="serif">Online Booking Apps</h3><p>Lorem ipsum dolor sit amet, consectetur adipiscing elit, sed do eiusmod tempor incididunt ut nn</p><a>Read More</a></div>
</div>
<div class="abs svc-card" style="left:786px">
  <div class="svc-photo" style="background:linear-gradient(135deg,#e9f6fb,#8fb7c9 50%,#c7ebf8)" role="img" aria-label="Team reviewing marketing charts at a desk"></div>
  <div class="svc-box"><h3 class="serif">Services Marketing</h3><p>Lorem ipsum dolor sit amet, consectetur adipiscing elit, sed do eiusmod tempor incididunt ut nn</p><a>Read More</a></div>
</div>
<div class="abs outline-btn">Learn More</div>

<!-- why choose us -->
<div class="abs why"></div>
<div class="abs eyebrow why-head">Why choose us</div>
<h2 class="abs serif why-title">Connecting Brands with the Digital Pulse</h2>
<p class="abs body-copy why-copy">Lorem ipsum dolor sit amet, consectetur adipiscing elit, sed do eiusmo d tempor incididunt ut labore et dolore magna aliqua. Ut enim ad min im veniam, quis nostrud exercitation jj</p>

<div class="abs why-item" style="left:106px;top:2880px">
  <svg width="30" height="30" viewBox="0 0 30 30" style="flex:none"><rect x="2" y="4" width="8" height="6" fill="none" stroke="#00a9dd" stroke-width="2"/><rect x="2" y="20" width="8" height="6" fill="none" stroke="#00a9dd" stroke-width="2"/><rect x="20" y="12" width="8" height="6" fill="none" stroke="#00a9dd" stroke-width="2"/><path d="M10 7h5v16h-5M15 15h5" stroke="#00a9dd" stroke-width="2" fill="none"/></svg>
  <div><h4>Client-centric</h4><p>Lorem ipsum dolor sit amet, consectetur adipiscing elit.</p></div>
</div>
<div class="abs why-item" style="left:370px;top:2880px">
  <svg width="30" height="30" viewBox="0 0 30 30" style="flex:none"><circle cx="15" cy="6" r="3" fill="#00a9dd"/><path d="M4 12h22M15 12v8l-6 8M15 20l6 8" stroke="#00a9dd" stroke-width="2" fill="none"/></svg>
  <div><h4>Personalized Approach</h4><p>Lorem ipsum dolor sit amet, consectetur adipiscing elit.</p></div>
</div>
<div class="abs why-item" style="left:106px;top:2976px">
  <svg width="30" height="30" viewBox="0 0 30 30" style="flex:none"><circle cx="8" cy="10" r="4" fill="#00a9dd"/><path d="M2 22a6 6 0 0 1 12 0z" fill="#00a9dd"/><path d="M16 9h12M16 15h12M16 21h12" stroke="#00a9dd" stroke-width="2"/></svg>
  <div><h4>Proven Track Record</h4><p>Lorem ipsum dolor sit amet, consectetur adipiscing elit.</p></div>
</div>
<div class="abs why-item" style="left:370px;top:2976px">
  <svg width="30" height="30" viewBox="0 0 30 30" style="flex:none"><rect x="3" y="16" width="5" height="11" fill="#00a9dd"/><rect x="12" y="11" width="5" height="16" fill="#00a9dd"/><rect x="21" y="6" width="5" height="21" fill="#00a9dd"/><path d="M3 12l9-6 9 2 6-6" stroke="#00a9dd" stroke-width="2" fill="none"/></svg>
  <div><h4>Quality Services</h4><p>Lorem ipsum dolor sit amet, consectetur adipiscing elit.</p></div>
</div>

<svg class="abs" style="left:638px;top:2612px" width="476" height="486" viewBox="0 0 476 486">
  <path d="M30 300 A222 222 0 0 1 430 120" fill="none" stroke="#0094d4" stroke-width="8"/>
  <path d="M460 160 A222 222 0 0 1 410 390" fill="none" stroke="#0094d4" stroke-width="14"/>
</svg>
<div class="abs" style="left:650px;top:2640px;width:446px;height:446px;border-radius:50%;background:radial-gradient(circle at 65% 40%,#c98aa6,#2f6d92 45%,#0a2f4a 85%)" role="img" aria-label="Woman working at a computer in a dim office"></div>

<!-- reviews -->
<div class="abs rev-head"><div class="eyebrow">Testimonials</div></div>
<h2 class="abs serif rev-title">Client Reviews</h2>

<div class="abs review" style="left:90px"><div class="avatar" role="img" aria-label="Client portrait"></div><div class="stars">★★★★★</div><p>Lorem ipsum dolor sit amet, consectetur adipiscing elit, sed do eiusmod tempor incididunt ut labore et dolore</p><div class="quote">“</div></div>
<div class="abs review" style="left:440px"><div class="avatar" role="img" aria-label="Client portrait"></div><div class="stars">★★★★★</div><p>Lorem ipsum dolor sit amet, consectetur adipiscing elit, sed do eiusmod tempor incididunt ut labore et dolore</p><div class="quote">“</div></div>
<div class="abs review" style="left:790px"><div class="avatar" role="img" aria-label="Client portrait"></div><div class="stars">★★★★★</div><p>Lorem ipsum dolor sit amet, consectetur adipiscing elit, sed do eiusmod tempor incididunt ut labore et dolore</p><div class="quote">“</div></div>
<div class="abs rev-name" style="left:90px">Noel Brandt<small>Country</small></div>
<div class="abs rev-name" style="left:440px">Noel Brandt<small>Country</small></div>
<div class="abs rev-name" style="left:790px">Noel Brandt<small>Country</small></div>

<!-- contact -->
<div class="abs contact-band" role="img" aria-label="Bright modern office interior"></div>
<div class="abs contact-person" role="img" aria-label="Woman in a white blouse holding a tablet"></div>
<div class="abs form-card">
  <div class="form-inner">
    <h2>Book an appointment</h2>
    <p>Lorem ipsum dolor sit amet, consectetur adipiscing elit,<br>sed do eiusmod tempor incididunt ut</p>
    <div class="field">NAAM</div>
    <div class="field">EMAIL</div>
    <div class="field">BERICHT</div>
    <div class="submit">BOOK NOW</div>
  </div>
</div>

<!-- footer -->
<div class="abs foot-logo">Plombek</div>
<div class="abs follow">Follow Us <span class="soc"></span><span class="soc"></span><span class="soc"></span></div>
<div class="abs fcol" style="left:364px;top:4553px"><h5>Quick Links</h5><ul><li>Home</li><li>About Us</li><li>Services</li><li>Contact Us</li></ul></div>
<div class="abs fcol" style="left:585px;top:4553px">
  <h5>Contact us</h5>
  <div class="row"><svg width="14" height="18" viewBox="0 0 14 18"><path d="M7 0a7 7 0 0 1 7 7c0 5-7 11-7 11S0 12 0 7a7 7 0 0 1 7-7z" fill="#00a9dd"/><circle cx="7" cy="7" r="2.5" fill="#fff"/></svg><span>88 Harbor Lane<br>210 Quay Road</span></div>
  <div class="row"><svg width="16" height="16" viewBox="0 0 24 24"><path d="M6 2l4 4-2 3a12 12 0 0 0 7 7l3-2 4 4-3 4C10 22 2 14 2 5z" fill="#00a9dd"/></svg><span>1-555-010-7734</span></div>
  <div class="row"><svg width="16" height="12" viewBox="0 0 16 12"><rect width="16" height="12" fill="#00a9dd"/><path d="M0 0l8 6 8-6" stroke="#fff" fill="none"/></svg><span>hello@plombek-mail.example</span></div>
</div>
<div class="abs fcol" style="left:860px;top:4553px"><h5 style="border:none;width:auto">Subscribe to Newsletter</h5><p style="font-size:12px;color:#6f8393;line-height:18px;width:220px">Sign up for our newsletter to know the latest from us</p><div class="news-in"><span>Email</span><b>VERSTUUR</b></div></div>
<div class="abs foot-line"></div>
<div class="abs copy">Plombek</div>

</body>
</html>
```